Business Card Design Project

We are a distribution company providing goods to Latin America. We sell everything from Medical equipment, generic medicines, to carecliners. The logo that we use is attached. The logo can incorporate different colors other than black for versatility. The company name is Valdoria International Corporation and/or VIC. The card will be printed using 1 or more of the following: Silk mounted and/or embossed. So if the design ideas could be made to incorporate that technique or any other unique techniques, it would be great. The target market is dialysis centers/doctors.

Basic Info for card:
Marnie Dowsett
Purchasing Manager
555-317-4086 direct
555-241-7953 fax
marnie.dowsett@valdoriavic.example
www.valdoriavic.example

Target Market(s)

Latin America

Industry/Entity Type

Business

Requirements
Nice to have
• The Front of the card should have the basic contact information with company name/logo. The back of the card could incorporate

```html
<!DOCTYPE html>
<html lang="en">
<head>
<meta charset="utf-8">
<title>Valdoria International Corporation – Business Card</title>
<link rel="stylesheet" href="https://fonts.googleapis.com/css2?family=Open+Sans:wght@400&display=swap">
<style>
  :root {
    --backdrop: #000000;
    --card: #ffffff;
    --ink: #1a1a1a;
    --mark: #111111;
  }
  html, body {
    margin: 0;
    padding: 0;
    width: 1200px;
    height: 900px;
    overflow: hidden;
    background: var(--backdrop);
  }
  .canvas {
    position: relative;
    width: 1200px;
    height: 900px;
    background: var(--backdrop);
  }
  .business-card {
    position: absolute;
    left: 259px;
    top: 231px;
    width: 684px;
    height: 360px;
    background: var(--card);
    border-radius: 2px;
    font-family: "Open Sans", sans-serif;
    color: var(--ink);
  }
  .brand {
    position: absolute;
    left: 485px;
    top: 40px;
    transform: translateX(-50%);
    display: flex;
    flex-direction: column;
    align-items: center;
    white-space: nowrap;
  }
  .brand-mark {
    width: 84px;
    height: 84px;
    border-radius: 50%;
    background: var(--mark);
  }
  .brand-name {
    margin-top: 27px;
    font-size: 18.5px;
    font-weight: 400;
    letter-spacing: 0.1px;
    line-height: 1;
  }
  .contact {
    position: absolute;
    left: 32px;
    top: 159px;
    font-size: 17px;
    line-height: 22px;
  }
  .contact p {
    margin: 0 0 22px 0;
  }
  .contact p:last-child {
    margin-bottom: 0;
  }
  .contact span {
    display: block;
  }
</style>
</head>
<body>
<main class="canvas">
  <section class="business-card">
    <div class="brand">
      <div class="brand-mark" role="img" aria-label="Valdoria International Corporation emblem"></div>
      <div class="brand-name">Valdoria International Corporation</div>
    </div>
    <div class="contact">
      <p>
        <span class="person-name">Marnie Dowsett</span>
        <span class="person-title">Purchasing Manager</span>
      </p>
      <p>
        <span class="phone-direct">555-317-4086 direct</span>
        <span class="phone-fax">555-241-7953 fax</span>
      </p>
      <p>
        <span class="email">marnie.dowsett@valdoriavic.example</span>
        <span class="website">www.valdoriavic.example</span>
      </p>
    </div>
  </section>
</main>
</body>
</html>
```